演奏会のメイン曲は、ベネディクト・ハウエル作曲「ラ・フォンテ・ヴェルデ」です。
演奏会全体としては、”希望の光”をイメージしています。
依然コロナ禍にありますが、音楽が”希望の光”になれば…
また、西海沿岸大洪水から10年で、復興支援のために作られた曲も演奏を予定しています。
・団体名
・演奏会名:ハーモニーフェスタ2021
・指揮者名:柳沼俊哉
・場所
・日時:2021年12月12日(日)
・曲目:ラ・フォンテ・ヴェルデ、星は今も瞬く、マルコの幻想の朝、夢にさそわれて…他
・問い合わせ先:担当/水野 090-2716-4098、https://sakuragi-brass.hoshizora-web.com/
など
※場所、チケット情報などは、添付画像と変化なしです。ご覧いただければと思います。
A4
片面
過去のチラシデータを添付いたしますので、ご参照ください。
チラシのデザインが決まれば、チラシのデザインを基に、チケット・ポスター・パンフレットの表紙も追加(1万程度)で作成していただきたいと考えております。
よろしくお願いします。
たくさんのご提案、ありがとうございます。
どれも素敵なデザインで、迷ってしまうという嬉しい悩みです。
わたし個人では決められないため、団体内で相談しようと思います。
相談できる日がお盆明けになる関係で、締め切りを延長しました。
引き続きよろしくお願いいたします。

クリスマスが近い時期の演奏会、という雰囲気に心惹かれました。
また、おしゃれさや見やすさ、演奏会全体の「希望に満ちたイメージ」との相性も含め、こちらのデザインに決めさせていただきました。

すてきなデザインをたくさんご応募いただき、本当にありがとうございました。
他のデザインにも、とても心惹かれました。
またよろしくお願いいたします。

```html
<!DOCTYPE html>
<html lang="ja">
<head>
<meta charset="UTF-8">
<title>ハーモニーフェスタ2021</title>
<link rel="stylesheet" href="https://fonts.googleapis.com/css2?family=Shippori+Mincho:wght@500;700;800&family=Noto+Sans+JP:wght@400;500;700&display=swap">
<style>
  :root {
    --sky-top: #cfc6e2;
    --sky-mid: #ece6f1;
    --glow: #fffbe8;
    --hill-light: #a9b98a;
    --hill-mid: #6f8757;
    --hill-dark: #3f5a3a;
    --title: #4a3a6e;
    --ink: #2d2a3a;
    --white: #ffffff;
    --label-bg: #3f3a52;
    --footer-bg: #ffffff;
    --map-fill: #e9e7ee;
  }
  * { margin: 0; padding: 0; box-sizing: border-box; }
  html, body { width: 849px; height: 1200px; overflow: hidden; background: #fff; }
  .poster {
    position: relative; width: 849px; height: 1200px; overflow: hidden;
    font-family: "Shippori Mincho", serif; color: var(--ink);
  }
  .landscape-photo {
    position: absolute; inset: 0 0 225px 0;
    background:
      radial-gradient(ellipse 260px 200px at 50% 36%, rgba(255,251,232,0.95), rgba(255,251,232,0) 70%),
      linear-gradient(180deg, var(--sky-top) 0%, var(--sky-mid) 22%, #f3efe6 32%, var(--hill-light) 48%, var(--hill-mid) 70%, var(--hill-dark) 100%);
  }
  .org-name {
    position: absolute; top: 36px; width: 100%; text-align: center;
    font-size: 32px; font-weight: 700; letter-spacing: 4px; color: var(--title);
  }
  .event-title {
    position: absolute; top: 100px; width: 100%; text-align: center;
    font-weight: 800; color: var(--title); line-height: 1.18; font-size: 62px; letter-spacing: 4px;
  }
  .event-title .year { font-size: 34px; letter-spacing: 1px; margin-left: 8px; }
  .event-date {
    position: absolute; top: 252px; width: 100%; text-align: center; color: var(--title);
  }
  .event-date .day { font-size: 52px; font-weight: 800; letter-spacing: 2px; }
  .event-date .weekday { font-size: 24px; font-weight: 700; }
  .event-date .times { display: block; font-size: 21px; font-weight: 700; letter-spacing: 1px; margin-top: 2px; }
  .event-date .times span { margin: 0 10px; }
  .programme {
    position: absolute; top: 410px; width: 100%; text-align: center; color: var(--white);
    text-shadow: 0 1px 4px rgba(40,50,30,0.6);
  }
  .programme .label { font-size: 19px; font-weight: 700; letter-spacing: 4px; }
  .programme .conductor { font-size: 30px; font-weight: 700; letter-spacing: 6px; margin: 2px 0 26px; }
  .programme ul { list-style: none; font-size: 22px; font-weight: 700; line-height: 1.55; }
  .ticket {
    position: absolute; top: 738px; width: 100%; text-align: center; color: var(--white);
    text-shadow: 0 1px 4px rgba(30,40,25,0.7);
  }
  .ticket .seat { font-size: 16px; font-weight: 700; }
  .ticket .price { font-size: 44px; font-weight: 800; margin-left: 6px; }
  .ticket .note { display: block; font-family: "Noto Sans JP", sans-serif; font-size: 13px; margin-top: 4px; }
  .footer {
    position: absolute; left: 0; right: 0; bottom: 0; height: 225px; background: var(--footer-bg);
    font-family: "Noto Sans JP", sans-serif;
  }
  .info { position: absolute; left: 44px; top: 14px; width: 440px; }
  .info-row { margin-bottom: 8px; }
  .info-label {
    display: inline-block; background: var(--label-bg); color: var(--white);
    font-size: 12px; font-weight: 500; line-height: 1.4; padding: 1px 10px; margin-bottom: 2px;
  }
  .phone { display: flex; align-items: center; gap: 8px; font-size: 32px; font-weight: 700; letter-spacing: 1px; line-height: 1.1; }
  .url { font-size: 13px; line-height: 1.4; }
  .venue { font-family: "Shippori Mincho", serif; font-size: 22px; font-weight: 700; line-height: 1.3; }
  .address { font-size: 12px; line-height: 1.5; }
  .venue-map {
    position: absolute; right: 18px; top: 10px; width: 310px; height: 205px;
    background: var(--map-fill); border: 1px solid #cfcbd8;
  }
</style>
</head>
<body>
<main class="poster">
  <div class="landscape-photo" role="img" aria-label="陽光が差し込む緑の渓谷と一本の道、淡い紫の空に音符が浮かぶ風景写真"></div>

  <p class="org-name">桜木市民吹奏楽団</p>
  <h1 class="event-title">ハーモニー<br>フェスタ<span class="year">2021</span></h1>
  <p class="event-date">
    <span class="day">12.12</span><span class="weekday">(日)</span>
    <span class="times"><span>開場 13:30</span><span>開演 14:00</span><span>終演 16:00</span></span>
  </p>

  <section class="programme">
    <p class="label">指揮</p>
    <p class="conductor">柳沼俊哉</p>
    <p class="label">曲目</p>
    <ul>
      <li>ラ・フォンテ・ヴェルデ</li>
      <li>星は今も瞬く</li>
      <li>マルコの幻想の朝</li>
      <li>夢にさそわれて</li>
      <li>…他</li>
    </ul>
  </section>

  <p class="ticket">
    <span class="seat">【全席自由・前売当日共通】</span><span class="price">¥500</span>
    <span class="note">収益の一部は西海沿岸大洪水の復興支援に寄付いたします</span>
  </p>

  <footer class="footer">
    <div class="info">
      <div class="info-row">
        <span class="info-label">お問い合わせ 担当/水野</span>
        <p class="phone">
          <svg width="24" height="24" viewBox="0 0 24 24" aria-hidden="true"><path fill="#2d2a3a" d="M6.6 10.8a15.1 15.1 0 0 0 6.6 6.6l2.2-2.2a1 1 0 0 1 1-.25 11.4 11.4 0 0 0 3.6.57 1 1 0 0 1 1 1V20a1 1 0 0 1-1 1A17 17 0 0 1 3 4a1 1 0 0 1 1-1h3.5a1 1 0 0 1 1 1c0 1.25.2 2.45.57 3.57a1 1 0 0 1-.25 1z"/></svg>
          090-2716-4098
        </p>
        <p class="url">https://sakuragi-brass.hoshizora-web.com/</p>
      </div>
      <div class="info-row">
        <span class="info-label">会場</span>
        <p class="venue">桜木市文化会館</p>
        <p class="address">桜木市緑ヶ丘町3丁目12番地<br>桜木駅より徒歩15分・駐車場あり</p>
      </div>
    </div>
    <div class="venue-map" role="img" aria-label="桜木市文化会館周辺の案内地図"></div>
  </footer>
</main>
</body>
</html>
```